Buch-/E-Book-Cover für High Fantasyromanen
Ausgesprochen nette und unkomplizierte Zusammenarbeit und ein wunderschönes Design für mein Buch-Cover!
Zielgruppe
Ich bin Autorin. Meine Zielgruppe sind Leser von High Fantasyromanen.
Aufgabenstellung
Ich möchte keine fotorealistischen Darstellungen. Figuren von Personen sollen, nur angedeutet werden. zB in der Silhouette dargestellt. Ich füge ein Briefing mit Hintergrund und Inhalt an.

```html
<!DOCTYPE html>
<html lang="de">
<head>
<meta charset="utf-8">
<title>Die Glut von Elvarin – Buchcover</title>
<link rel="stylesheet" href="https://fonts.googleapis.com/css2?family=Cormorant+Garamond:wght@400;500&family=Uncial+Antiqua&display=swap">
<style>
  :root {
    --page-bg: #e9e7e3;
    --forest-dark: #18171b;
    --forest-mid: #35322a;
    --trunk: #2a2822;
    --forest-glow: #b3a762;
    --forest-light: #e6dca8;
    --bloom-violet: #7a4fb0;
    --title-magenta: #e4157c;
    --text-light: #f2efe6;
  }
  * { margin: 0; padding: 0; box-sizing: border-box; }
  html, body {
    width: 1200px;
    height: 800px;
    overflow: hidden;
    background: var(--page-bg);
  }
  .stage {
    width: 1200px;
    height: 800px;
    display: flex;
    align-items: center;
    justify-content: center;
  }
  .book-cover {
    position: relative;
    width: 494px;
    height: 740px;
    overflow: hidden;
    background: var(--forest-dark);
    box-shadow: 0 10px 30px rgba(0, 0, 0, 0.25);
  }
  .cover-artwork {
    position: absolute;
    inset: 0;
    background:
      radial-gradient(ellipse 22% 55% at 55% 62%, rgba(24, 23, 27, 0.85) 0%, rgba(24, 23, 27, 0) 75%),
      radial-gradient(ellipse 40% 38% at 82% 48%, var(--forest-light) 0%, rgba(230, 220, 168, 0) 72%),
      radial-gradient(ellipse 26% 30% at 14% 66%, rgba(230, 220, 168, 0.65) 0%, rgba(230, 220, 168, 0) 72%),
      radial-gradient(ellipse 55% 18% at 35% 100%, rgba(122, 79, 176, 0.6) 0%, rgba(122, 79, 176, 0) 72%),
      linear-gradient(165deg, var(--forest-dark) 0%, var(--forest-mid) 30%, var(--forest-glow) 55%, var(--trunk) 82%, var(--forest-dark) 100%);
  }
  .cover-text {
    position: absolute;
    left: 150px;
    right: 16px;
    bottom: 40px;
    color: var(--text-light);
  }
  .author-name {
    font-family: "Cormorant Garamond", serif;
    font-weight: 500;
    font-size: 22px;
    letter-spacing: 0.22em;
    margin-bottom: 10px;
    white-space: nowrap;
  }
  .book-title {
    font-family: "Uncial Antiqua", serif;
    font-weight: 400;
    font-size: 42px;
    line-height: 1.05;
    color: var(--title-magenta);
    white-space: nowrap;
  }
  .book-title .title-line { display: block; }
  .book-title .title-line.second { padding-left: 40px; }
  .book-subtitle {
    font-family: "Cormorant Garamond", serif;
    font-weight: 500;
    font-size: 21px;
    letter-spacing: 0.12em;
    margin-top: 12px;
    white-space: nowrap;
  }
</style>
</head>
<body>
  <main class="stage">
    <article class="book-cover">
      <div class="cover-artwork" role="img" aria-label="Gemalte Fantasy-Illustration: ein mächtiger alter Baum in goldenem Waldlicht, davor eine Figur in Kapuzenmantel von hinten als Silhouette, Schmetterlinge, fallendes Laub und violette Blüten am Boden"></div>
      <div class="cover-text">
        <p class="author-name">Joline Brecht</p>
        <h1 class="book-title">
          <span class="title-line">die Glut</span>
          <span class="title-line second">von Elvarin</span>
        </h1>
        <p class="book-subtitle">das Raunen der Wälder</p>
      </div>
    </article>
  </main>
</body>
</html>
```